A specialised Sport management needs a corporate brochure design

We are a specialized company in the management and consultancy of sports events. and need to have a company brochure
We provide the following services;
Event management
Venues management
Production
Ticketing
Consulting
Hospitality
Activity management
Event timing
Branding of event
Event supplies
We need a corporate profile design for our company to showcase the major events that we have covered , with images, information, statistics, surveys, products and services used. We want to highlight our professionalism and execution of the events, experience of the participants, spectators . How we have grown in the past few years and reached the international standards.
Objectives of the work:
To get sponsors and partners for future business and to present Keel-Marrow
as not just a sports management company but also a professional sports
events management company.
You can check our website
www.keel-marrow.example
Target Market(s)
Sponsors and corporate partners
Industry/Entity Type
Events
Font styles to use
Requirements
Must have
- Must Have:
- - Very professional look
- -Some event images,Event information, statistics, surveys, products and services used. We want to highlight our professionalism and execution of the events (Attached)
Nice to have
- Similar momentom of the below design
- http://www.dunlathgames.example/wp-content/themes/dunlath_games/pdf/CP-2014-15-V10-Web.pdf

```html
<!DOCTYPE html>
<html lang="en">
<head>
<meta charset="utf-8">
<title>Keel-Marrow Sport Management – Corporate Brochure</title>
<link rel="stylesheet" href="https://fonts.googleapis.com/css2?family=Barlow:wght@400;500;700;800&family=Barlow+Condensed:wght@700;800&display=swap">
<style>
  :root{
    --orange:#f15a22;
    --orange-dark:#d94a15;
    --green:#1d6b3b;
    --grey:#7d7d7d;
    --grey-light:#b9b9b9;
    --ink:#4a4a4a;
    --paper:#ffffff;
    --backdrop:#e9e6e1;
  }
  *{box-sizing:border-box;margin:0;padding:0}
  html,body{width:1200px;height:800px;overflow:hidden}
  body{background:var(--backdrop);font-family:'Barlow',Arial,sans-serif;position:relative}

  .page{position:absolute;width:538px;height:345px;overflow:hidden;background:var(--paper);box-shadow:0 2px 8px rgba(0,0,0,.18)}
  .page--about{left:52px;top:40px}
  .page--cover{left:610px;top:40px}
  .page--quote{left:52px;top:415px}
  .page--segment{left:610px;top:415px}

  .photo{position:absolute}
  .photo--race{inset:0;background:radial-gradient(ellipse at 55% 55%,#8e8f93 0%,#c9c7c4 38%,#e5e2de 70%,#d2d0cd 100%)}
  .photo--rope{inset:0;background:linear-gradient(160deg,#c4cddc 0%,#d9dfe8 55%,#e3e6ec 100%)}
  .photo--rocks{inset:0;background:linear-gradient(180deg,#3a63b3 0%,#6e8cc2 18%,#c8b59a 34%,#b49e80 65%,#8f7a5f 100%)}
  .photo--strip{left:0;top:0;width:175px;height:345px;background:linear-gradient(180deg,#3d6bb8 0%,#7da0cf 22%,#c0aa8a 40%,#a88f6f 100%)}

  /* about page */
  .sidebar{position:absolute;left:31px;top:0;width:134px;height:345px;background:var(--orange);color:#fff}
  .wordmark{font-weight:800;letter-spacing:.02em;line-height:1;white-space:nowrap}
  .sidebar .wordmark{position:absolute;left:12px;top:74px;font-size:14px;color:#fff;display:flex;align-items:center;gap:5px}
  .wordmark .dot{width:9px;height:9px;border-radius:50%;background:currentColor;flex:none}
  .about{position:absolute;left:12px;top:154px;width:112px}
  .about h2{font-size:10.5px;font-weight:700;line-height:1.2}
  .about p{font-size:8.6px;line-height:1.22;margin-top:1px}
  .sidebar .url{position:absolute;left:12px;top:307px;font-size:8.5px;font-weight:700;line-height:1}
  .goal{position:absolute;left:195px;top:26px;width:292px;color:var(--orange)}
  .goal h2{font-size:11px;font-weight:700}
  .goal p{font-size:9.4px;line-height:1.25;margin-bottom:9px}

  /* cover */
  .cover-mark{position:absolute;right:40px;top:62px;color:var(--grey);font-size:22px;display:flex;align-items:center;gap:8px}
  .cover-mark .dot{width:14px;height:14px;border-radius:50%;background:var(--orange)}
  .headline{position:absolute;right:30px;top:268px;text-align:right;font-family:'Barlow Condensed','Arial Narrow',sans-serif;font-weight:800;line-height:.9}
  .headline .l1{color:var(--orange);font-size:30px;display:block;margin-right:54px}
  .headline .l2{color:var(--grey);font-size:22px}
  .headline .l3{color:var(--green);font-size:32px}

  /* quote */
  .quote{position:absolute;left:181px;top:85px;width:177px;height:177px;background:var(--orange);color:#fff;text-align:center;padding:28px 16px 0}
  .quote .mark{font-size:16px;font-weight:800;line-height:1}
  .quote blockquote{font-size:9.2px;font-weight:700;line-height:1.3;margin:4px 0}
  .quote .who{font-size:7.5px;margin-top:18px;line-height:1.3}

  /* segment */
  .stat{position:absolute;left:124px;width:98px;height:98px;border-radius:50%;background:var(--orange);border:3px solid #fff;color:#fff;text-align:center;display:flex;flex-direction:column;justify-content:center;padding:0 12px}
  .stat__head{font-size:9px;line-height:1.15}
  .stat__note{font-size:6.6px;line-height:1.2;margin-top:6px;color:#fde3d6}
  .stat__value{font-size:10px;font-weight:700;margin-top:1px}
  .band{position:absolute;left:205px;top:0;width:333px;height:30px;background:var(--orange);color:#fff;font-size:13px;font-weight:700;padding:8px 0 0 34px}
  .col{position:absolute;top:42px;color:var(--ink);font-size:9px;line-height:1.2}
  .col h3{color:var(--orange);font-size:10px;font-weight:700}
  .col--main{left:240px;width:128px}
  .col--side{left:380px;width:125px}
  .col--side h3 + p{margin-bottom:11px}
  .growth{position:absolute;left:240px;top:196px;width:267px}
  .growth h3{color:var(--green);font-size:10px;font-weight:700;border-bottom:1px solid #8c8c8c;padding-bottom:2px;display:flex}
  .growth h3 span{background:#fff;padding-right:4px;margin-bottom:-9px}
  .row{display:flex;align-items:center;height:26px}
  .row:first-of-type{margin-top:9px}
  .year{background:var(--green);color:#fff;font-size:8.5px;font-weight:700;width:34px;height:15px;padding:2px 0 0 3px;clip-path:polygon(0 0,82% 0,100% 50%,82% 100%,0 100%)}
  .count{font-size:8.5px;color:var(--ink);width:86px;padding-left:5px}
  .people{display:flex;gap:2.5px}
  .people svg{width:9px;height:17px}
  .on{fill:var(--orange)} .off{fill:var(--grey-light)}
</style>
</head>
<body>
<svg width="0" height="0" style="position:absolute">
  <symbol id="person" viewBox="0 0 9 17"><circle cx="4.5" cy="2" r="2"/><path d="M1 4.5h7v6H6.6V17H5V11.5H4V17H2.4V10.5H1z"/></symbol>
</svg>

<section class="page page--about">
  <div class="photo photo--race" role="img" aria-label="Race car drifting through thick tyre smoke"></div>
  <aside class="sidebar">
    <div class="wordmark"><span class="dot"></span>KEEL-MARROW</div>
    <div class="about">
      <h2>About Us</h2>
      <p>Keel-Marrow is the leading company in Kuwait, which specializes in the management and consultancy of sports events. Established in 2007, Keel-Marrow has grown in stature and strength over the years, to become the reowned establishment it is today in this highly specialized field.</p>
    </div>
    <span class="url">www.keel-marrow.example</span>
  </aside>
  <div class="goal">
    <h2>Our Goal</h2>
    <p>Raise awareness of sport practice and creating exciting sport events with international standards. Allowing every individual to participate in different types of sport events for all levels.</p>
    <p>Each year we get closer to our goal to promote active lifestyle and sports activities in the country. We believe our partners play a major role in the contribution towards our goal for the society.</p>
  </div>
</section>

<section class="page page--cover">
  <div class="photo photo--rope" role="img" aria-label="Athlete's taped arm gripping a thick climbing rope against the sky"></div>
  <div class="wordmark cover-mark"><span class="dot"></span>KEEL-MARROW</div>
  <h1 class="headline"><span class="l1">Let’s take care</span><span class="l2">of your next </span><span class="l3">sports event!</span></h1>
</section>

<section class="page page--quote">
  <div class="photo photo--rocks" role="img" aria-label="Runner in a race bib climbing down rocky desert terrain with marshals behind"></div>
  <figure class="quote">
    <div class="mark">“</div>
    <blockquote>Haven’t tried any Event managers before Keel-Marrow, don’t want to try any others</blockquote>
    <div class="mark">”</div>
    <figcaption class="who">Faris Alwadi<br>Founder Lapline+</figcaption>
  </figure>
</section>

<section class="page page--segment">
  <div class="photo photo--strip" role="img" aria-label="Rocky desert course under a blue sky"></div>
  <div class="stat" style="top:18px"><div class="stat__head">Number of participates in 2014 10,000</div><div class="stat__note">Said they would rate our events as 'Excellent' in our survey (average)</div><div class="stat__value">86%</div></div>
  <div class="stat" style="top:129px"><div class="stat__head">Number of sports 13</div><div class="stat__note">Said they would participate again (average)</div><div class="stat__value">84%</div></div>
  <div class="stat" style="top:240px"><div class="stat__head">Visitors 30,000</div><div class="stat__note">Said they recognized our sponsors (average)</div><div class="stat__value">80%</div></div>

  <h2 class="band">Target Segment</h2>
  <div class="col col--main">
    <h3>Mainstream Public</h3>
    <p>This is a huge audience reached predominantly through the mainstream print and digital coverage. They are captivated and inspired by the incredible feats of sport events and determination displayed by the athletes. Estimated number of mainstream audience is 50,000</p>
  </div>
  <div class="col col--side">
    <h3>Engaged</h3>
    <p>This segment encompasses all those who are engaged directly with us, but not necessarily a current athlete.</p>
    <h3>Athletes</h3>
    <p>Majority of athletes are ranging between 20 - 45 years old, %70 Male and %30 Female , with high disposable incomes. They are fit, motivated and looking to challenge themselves.</p>
  </div>

  <div class="growth">
    <h3><span>Growth Over the Years</span></h3>
    <div class="row"><span class="year">2011</span><span class="count">Participants 1,300</span><span class="people">
      <svg class="on"><use href="#person"/></svg><svg class="off"><use href="#person"/></svg><svg class="off"><use href="#person"/></svg><svg class="off"><use href="#person"/></svg><svg class="off"><use href="#person"/></svg><svg class="off"><use href="#person"/></svg><svg class="off"><use href="#person"/></svg><svg class="off"><use href="#person"/></svg><svg class="off"><use href="#person"/></svg><svg class="off"><use href="#person"/></svg><svg class="off"><use href="#person"/></svg><svg class="off"><use href="#person"/></svg></span></div>
    <div class="row"><span class="year">2012</span><span class="count">Participants 2,700</span><span class="people">
      <svg class="on"><use href="#person"/></svg><svg class="on"><use href="#person"/></svg><svg class="on"><use href="#person"/></svg><svg class="off"><use href="#person"/></svg><svg class="off"><use href="#person"/></svg><svg class="off"><use href="#person"/></svg><svg class="off"><use href="#person"/></svg><svg class="off"><use href="#person"/></svg><svg class="off"><use href="#person"/></svg><svg class="off"><use href="#person"/></svg><svg class="off"><use href="#person"/></svg><svg class="off"><use href="#person"/></svg></span></div>
    <div class="row"><span class="year">2013</span><span class="count">Participants 5,800+</span><span class="people">
      <svg class="on"><use href="#person"/></svg><svg class="on"><use href="#person"/></svg><svg class="on"><use href="#person"/></svg><svg class="on"><use href="#person"/></svg><svg class="on"><use href="#person"/></svg><svg class="on"><use href="#person"/></svg><svg class="on"><use href="#person"/></svg><svg class="off"><use href="#person"/></svg><svg class="off"><use href="#person"/></svg><svg class="off"><use href="#person"/></svg><svg class="off"><use href="#person"/></svg><svg class="off"><use href="#person"/></svg></span></div>
    <div class="row"><span class="year">2014</span><span class="count">Participants 10,000+</span><span class="people">
      <svg class="on"><use href="#person"/></svg><svg class="on"><use href="#person"/></svg><svg class="on"><use href="#person"/></svg><svg class="on"><use href="#person"/></svg><svg class="on"><use href="#person"/></svg><svg class="on"><use href="#person"/></svg><svg class="on"><use href="#person"/></svg><svg class="on"><use href="#person"/></svg><svg class="on"><use href="#person"/></svg><svg class="on"><use href="#person"/></svg><svg class="on"><use href="#person"/></svg><svg class="on"><use href="#person"/></svg></span></div>
  </div>
</section>
</body>
</html>
```